BATH BOMB BAG SET UP 10 x 14 CM

Hi.
I need a bath bomb bag set up. I've uploaded an example of the type of bag im getting as well as my vision (as best I could) to help you create it.
NOTES :
-clean and modern appearance
-set up for printing
- for the color I'm thinking not black, but a dark grey- like an antique black on fabiric of that makes sense ?
-10 x 14 CM bag size
FRONT SIDE paragraph :
Small batch-crafted with intention and embodying phytonutrients and botanical compounds with natural medicinal properties to relax and relieve the mind and body
BACK SIDE will contain all the warnings and icons ::
(pregnancy warning should be outlined/within box) WARNING: USE BY PREGNANT OR BREASTFEEDING WOMEN, OR BY WOMEN PLANNING TO BECOME PREGNANT, MAY RESULT IN FETAL INJURY, PRETERM BIRTH, LOW BIRTH WEIGHT, OR DEVELOPMENTAL PROBLEMS FOR THE CHILD.
WARNING :
FOR USE BY INDIVIDUALS 21 YEARS OF AGE OR OLDER OR REGISTERED QUALIFYING PATIENTS ONLY. IT IS ILLEGAL TO DRIVE A MOTOR VEHICLE WHILE UNDER THE INFLUENCE OF MARIJUANA.
KEEP OUT OF REACH OF CHILDREN.
CIVIC TOXIN RESPONSE BUREAU 1-800-555-0147
THE ACTUAL VALUE OF CANNABINOIDS MAY VARY FROM THW REPORTED VALUE BY +/- 15%.
ACTIVATION TIME : 20 - 45 MINUTES
WARNING: FOR EXTERNAL USE ONLY. THIS PRODUCT CONTAINS ESSENTIAL OILS. STOP USE IF IRRITATION OCCURS. CONSULT WITH A PHYSICIAN BEFORE USE ESPECIALLY IF YOU HAVE A MEDICAL CONDITION OR TAKING PRESCRIPTION MEDICATIONS OR IF PREGNANT OR NURSING.
SAFETY: USE CAUTION WHEN EXITING THE BATH. THESE SKIN LOVING OILS CAN MAKE THE TUB SLIPPERY.
Miriam's Fennel Co. ♡ KX T 004837
www.LOMWELTRY.INFO

```html
<!DOCTYPE html>
<html lang="en">
<head>
<meta charset="utf-8">
<title>Orla's THC Botanical Bath Bomb Bag</title>
<link href="https://fonts.googleapis.com/css2?family=Jost:wght@300;400;500;600;700&family=Poppins:wght@500;600&display=swap" rel="stylesheet">
<style>
  :root {
    --page: #ffffff;
    --ink: #2a2a2a;
    --trim: #bdbdbd;
  }
  * { margin: 0; padding: 0; box-sizing: border-box; }
  html, body {
    width: 1200px; height: 2400px; overflow: hidden;
    background: var(--page);
  }
  .sheet {
    position: absolute; left: 40px; top: 808px;
    width: 1120px; height: 784px;
    display: flex;
    border: 2px solid var(--trim);
  }
  .panel {
    position: relative; width: 560px; height: 100%;
    color: var(--ink);
    font-family: "Jost", sans-serif;
    text-align: center;
  }
  .panel--front { border-right: 2px solid var(--trim); }

  .legal-mark {
    position: absolute; width: 76px; height: 66px;
  }
  .panel--front .legal-mark { left: 370px; top: 137px; }
  .panel--back .legal-mark { left: 242px; top: 637px; }

  .brand-name {
    position: absolute; left: 0; right: 0; top: 214px;
    font-weight: 700; font-size: 38px; letter-spacing: 1px;
  }
  .product-thc {
    position: absolute; left: 0; right: 0; top: 286px;
    font-weight: 700; font-size: 150px; line-height: 1; letter-spacing: 10px;
    padding-left: 10px;
  }
  .product-kind {
    position: absolute; left: 0; right: 0; top: 440px;
    font-weight: 400; font-size: 42px; letter-spacing: 13px; padding-left: 13px;
  }
  .product-sub {
    position: absolute; left: 0; right: 0; top: 490px;
    font-weight: 500; font-size: 23px; letter-spacing: 6px; padding-left: 6px;
  }
  .product-story {
    position: absolute; left: 0; right: 0; top: 548px;
    font-weight: 300; font-size: 16.5px; line-height: 19.5px;
  }
  .product-tagline {
    position: absolute; left: 0; right: 0; top: 662px;
    display: flex; justify-content: center; gap: 30px;
    font-weight: 400; font-size: 14px; letter-spacing: 4px;
  }

  .badges {
    position: absolute; left: 0; right: 0; top: 168px;
    display: flex; justify-content: center; gap: 30px;
  }
  .badge {
    width: 100px; display: flex; flex-direction: column; align-items: center;
    font-family: "Poppins", sans-serif; font-weight: 500;
    font-size: 15px; line-height: 16px;
  }
  .badge svg { width: 40px; height: 40px; margin-bottom: 10px; }

  .notice {
    position: absolute; left: 36px; right: 36px;
    font-size: 8.6px; line-height: 12.5px; text-transform: uppercase;
  }
  .notice strong { font-weight: 700; font-size: 9px; }
  .notice--age { top: 272px; }
  .notice--pregnancy {
    top: 358px; left: 30px; right: 30px;
    font-size: 8.2px;
    border: 1.5px solid var(--ink); padding: 5px 2px;
  }
  .notice--external { top: 433px; }
  .notice--safety { top: 500px; }
  .maker {
    position: absolute; left: 0; right: 0; top: 542px;
    font-weight: 700; font-size: 11.5px; line-height: 18px;
  }
  .notice--potency { top: 592px; }
</style>
</head>
<body>
  <main class="sheet">
    <section class="panel panel--front" aria-label="Front of bag">
      <svg class="legal-mark" viewBox="0 0 76 66" role="img" aria-label="Regulatory warning triangle">
        <polygon points="3,3 73,3 38,63" fill="none" stroke="var(--ink)" stroke-width="5" stroke-linejoin="round"/>
      </svg>
      <div class="brand-name">ORLA'S</div>
      <div class="product-thc">THC</div>
      <div class="product-kind">BOTANICAL</div>
      <div class="product-sub">relieving bath bomb</div>
      <p class="product-story">small batch-crafted with intention and<br>embodying phytonutrients and botanical<br>compounds with natural medicinal properties<br>to relax and relieve the mind and body</p>
      <div class="product-tagline"><span>hydrate</span><span>indulge</span><span>pamper</span><span>relieve</span></div>
    </section>

    <section class="panel panel--back" aria-label="Back of bag">
      <div class="badges">
        <div class="badge">
          <svg viewBox="0 0 40 40" fill="none" stroke="var(--ink)" stroke-width="2" stroke-linecap="round" stroke-linejoin="round" aria-hidden="true">
            <circle cx="20" cy="20" r="15"/>
            <path d="M14 10 q6 -4 12 0 M31 22 q-1 7 -8 10 M9 24 q1 7 8 9"/>
            <path d="M17 21 q3 -7 9 -6 q0 7 -9 6z"/>
          </svg>
          <span>Natural<br>Ingredients</span>
        </div>
        <div class="badge">
          <svg viewBox="0 0 40 40" fill="none" stroke="var(--ink)" stroke-width="2" stroke-linecap="round" stroke-linejoin="round" aria-hidden="true">
            <path d="M20 34 C6 24 4 16 8 10 C12 5 18 7 20 12 C22 7 28 5 32 10 C36 16 34 24 20 34z"/>
            <path d="M15 24 q1 -9 10 -11 q0 9 -10 11z M15 24 l6 -6"/>
          </svg>
          <span>Vegan<br>Friendly</span>
        </div>
        <div class="badge">
          <svg viewBox="0 0 40 40" fill="none" stroke="var(--ink)" stroke-width="2" stroke-linecap="round" stroke-linejoin="round" aria-hidden="true">
            <path d="M15 5 h10 M17 5 v11 L8 33 h24 L23 16 V5"/>
            <path d="M12 26 h16"/>
          </svg>
          <span>Lab<br>Tested</span>
        </div>
      </div>

      <p class="notice notice--age"><strong>Warning :</strong><br>For use by individuals 21 years of age or older or registered qualifying patients only.<br>It is illegal to drive a motor vehicle while under the influence of marijuana.<br><br>Keep out of reach of children.<br>Civic Toxin Response Bureau 1-800-555-0147</p>

      <p class="notice notice--pregnancy"><strong>Warning:</strong><br>Use by pregnant or breastfeeding women, or by women planning to become pregnant,<br>may result in fetal injury, preterm birth, low birth weight, or developmental problems for the child.</p>

      <p class="notice notice--external"><strong>Warning:</strong><br>For external use only. This product contains essential oils. Stop use if irritation<br>occurs. Consult with a physician before use especially if you have a medical<br>condition or taking prescription medications or if pregnant or nursing.</p>

      <p class="notice notice--safety"><strong>Safety:</strong><br>Use caution when exiting the bath. These skin loving oils can make the tub slippery.</p>

      <p class="maker">Miriam's Fennel Co. KX T 004837<br>www.LOMWELTRY.INFO</p>

      <p class="notice notice--potency">The actual value of cannabinoids may vary from the reported value by +/- 15%.<br>Activation time : <strong>20 - 45 minutes</strong></p>

      <svg class="legal-mark" viewBox="0 0 76 66" role="img" aria-label="Regulatory warning triangle">
        <polygon points="3,3 73,3 38,63" fill="none" stroke="var(--ink)" stroke-width="5" stroke-linejoin="round"/>
      </svg>
    </section>
  </main>
</body>
</html>
```